Irrigation Business needs their business cards modernised and revamped

I would like to keep my current logo, colours and revamp the format of the card.

I would like the card to be clean yet important.

Im not sure if you include texture but i would like the named logo to be indented into the card etc.

show me something alive and free something thats clinical to the point yet has a feel of achievement. i would like people to go nice card.

Target Market(s)

high end clients, corporate, sports field manger, the guys that make the decisions

Industry/Entity Type

Business

Contact Information for Business Card

nformation to be included

Gareth Minchin (Director)
0472958316
gareth@tkwater.biz
www.tomskerrywatering.com

instagram logo
google logo
facebook logo

Colors

Designer to choose colors to be used in the design.

Requirements
Nice to have
• indentations a really nice feel to the card good texture

```html
<!DOCTYPE html>
<html lang="en">
<head>
<meta charset="utf-8">
<title>Tom's Kerry Watering – Business Card</title>
<link rel="stylesheet" href="https://fonts.googleapis.com/css2?family=Source+Sans+3:wght@400;600;700&display=swap">
<style>
  :root {
    --backdrop: #3b302c;
    --card: #141517;
    --card-edge: #1d1f22;
    --brand-blue: #3a73c4;
    --brand-sky: #3b9fd1;
    --brand-green: #3fae5a;
    --rule: #2aa6d6;
    --ink-light: #f1f3f5;
    --icon: #3a73c4;
    --social: #1f3f66;
    --social-ring: #2f5f99;
  }
  * { margin: 0; padding: 0; box-sizing: border-box; }
  html, body {
    width: 1200px; height: 864px; overflow: hidden;
    background: var(--backdrop);
    font-family: "Source Sans 3", "Myriad Pro", Arial, sans-serif;
  }
  .sheet { position: relative; width: 1200px; height: 864px; }
  .card {
    position: absolute;
    width: 550px; height: 314px;
    background: var(--card);
    border: 1px solid var(--card-edge);
    border-radius: 3px;
    box-shadow: 0 10px 24px rgba(0,0,0,0.45);
  }
  .card--front { left: 35px; top: 150px; }
  .card--back  { left: 615px; top: 400px; }

  /* Front */
  .front-mark__disc {
    position: absolute; left: 50%; top: 56px; transform: translateX(-50%);
    width: 160px; height: 160px; border-radius: 50%;
    background: var(--social);
    border: 3px solid var(--social-ring);
  }
  .social-links {
    position: absolute; left: 50%; top: 232px; transform: translateX(-50%);
    display: flex; gap: 7px;
  }
  .social-links span {
    width: 20px; height: 20px; border-radius: 50%;
    background: var(--social);
    border: 2px solid var(--social-ring);
  }

  /* Back */
  .contact { position: absolute; left: 34px; top: 116px; }
  .contact__name {
    font-weight: 700; font-size: 15px; color: var(--brand-blue);
    text-transform: uppercase; letter-spacing: 0.2px; line-height: 1.1;
  }
  .contact__role {
    font-weight: 400; font-size: 15px; color: var(--brand-green);
    text-transform: uppercase; line-height: 1.15;
  }
  .contact__rule {
    position: absolute; left: 34px; right: 30px; top: 160px;
    height: 1px; background: var(--rule);
  }
  .contact__list { position: absolute; left: 34px; top: 174px; list-style: none; }
  .contact__list li {
    display: flex; align-items: center; gap: 9px;
    color: var(--ink-light); font-size: 14.5px; line-height: 20px;
  }
  .contact__list svg { width: 11px; height: 11px; flex: none; }
  .brand {
    position: absolute; right: 30px; top: 52px;
    display: flex; flex-direction: column; align-items: center; gap: 8px;
  }
  .brand__disc {
    width: 56px; height: 56px; border-radius: 50%; background: var(--brand-sky);
  }
  .brand__name {
    font-weight: 700; font-size: 21px; line-height: 26px; color: var(--brand-blue);
    text-transform: uppercase; letter-spacing: 0.3px; white-space: nowrap;
  }
</style>
</head>
<body>
<main class="sheet">
  <section class="card card--front" aria-label="Card front">
    <div class="front-mark__disc"></div>
    <div class="social-links" aria-label="Social media links">
      <span></span><span></span><span></span>
    </div>
  </section>

  <section class="card card--back" aria-label="Card back">
    <div class="contact">
      <div class="contact__name">Gareth Minchin</div>
      <div class="contact__role">Director</div>
    </div>
    <div class="contact__rule"></div>
    <ul class="contact__list">
      <li>
        <svg viewBox="0 0 12 12"><path fill="var(--icon)" d="M2.5 1h2l1 2.5-1.3 1a6 6 0 0 0 3.3 3.3l1-1.3L11 7.5v2c0 .8-.7 1.5-1.5 1.5C5 11 1 7 1 2.5 1 1.7 1.7 1 2.5 1z"/></svg>
        0472958316
      </li>
      <li>
        <svg viewBox="0 0 12 12"><rect x="1" y="2.5" width="10" height="7" rx="1" fill="var(--icon)"/><path d="M1.5 3l4.5 3.5L10.5 3" stroke="var(--card)" stroke-width="1" fill="none"/></svg>
        gareth@tkwater.biz
      </li>
      <li>
        <svg viewBox="0 0 12 12"><circle cx="6" cy="6" r="5" fill="var(--icon)"/><path d="M1 6h10M6 1c-2.5 3-2.5 7 0 10M6 1c2.5 3 2.5 7 0 10" stroke="var(--card)" stroke-width="0.8" fill="none"/></svg>
        www.tomskerrywatering.com
      </li>
    </ul>
    <div class="brand">
      <div class="brand__disc"></div>
      <div class="brand__name">Tom's Kerry Watering</div>
    </div>
  </section>
</main>
</body>
</html>
```